Postcard Design

Marlow Painting-all types of painting and staining-house,deck and roof powerwashing-stone and masonry sealing-
30 years in business-licensed and insured
Ray Pettibone
pettiboneworks@brushmail.example
9145820731

Industry/Entity Type

Painting

```html
<!DOCTYPE html>
<html lang="en">
<head>
<meta charset="utf-8">
<title>Marlow Painting Postcard</title>
<link href="https://fonts.googleapis.com/css2?family=Cinzel:wght@400;700&family=Raleway:wght@400;500;700&display=swap" rel="stylesheet">
<style>
  :root {
    --purple-dark: #5a3a82;
    --purple: #7a4a94;
    --purple-light: #9a5aa6;
    --ink: #1d1d1d;
    --paper: #ffffff;
    --rule: #cfcfcf;
    --line: #222222;
    --green: #3fae3a;
    --logo-ink: #4b3a78;
  }
  * { box-sizing: border-box; margin: 0; padding: 0; }
  html, body { width: 849px; height: 1200px; overflow: hidden; background: var(--paper); }
  .sheet { position: relative; width: 849px; height: 1200px; }

  .card {
    position: absolute; left: 78px; width: 710px; height: 550px;
    border: 1px solid var(--rule); overflow: hidden; background: var(--paper);
  }
  .card--front { top: 32px; }
  .card--back { top: 601px; }

  /* front */
  .front__hero {
    position: absolute; left: 0; top: 0; width: 375px; height: 550px;
    background:
      radial-gradient(ellipse at 30% 15%, #e7c24a 0%, rgba(231,194,74,0) 45%),
      radial-gradient(ellipse at 80% 25%, #d8e04a 0%, rgba(216,224,74,0) 40%),
      radial-gradient(ellipse at 10% 55%, #e5542e 0%, rgba(229,84,46,0) 40%),
      linear-gradient(180deg, #c8a0c0 0%, #9bb86a 30%, #2fb044 55%, #e9ece6 75%, #ffffff 100%);
  }
  .front__headline {
    position: absolute; left: 0; top: 130px; width: 375px; text-align: center;
    font-family: "Cinzel", serif; font-weight: 400; font-size: 41px; line-height: 51px;
    color: var(--paper); letter-spacing: 0.5px;
  }
  .front__headline .c1 { color: #e8413f; }
  .front__headline .c2 { color: #f4d23a; }
  .front__headline .c3 { color: #4bb84a; }
  .front__headline .c4 { color: #3aa2d8; }
  .front__headline .c5 { color: #4a5fc0; }
  .front__tagline {
    position: absolute; left: 0; top: 238px; width: 375px; text-align: center;
    font-family: "Raleway", sans-serif; font-weight: 700; font-size: 15px;
    letter-spacing: 1.5px; color: var(--ink);
  }
  .front__photo {
    position: absolute; left: 375px; top: 0; width: 335px; height: 390px;
    background: linear-gradient(160deg, #d9cfc2 0%, #efe9e1 45%, #ffffff 90%);
  }
  .brand {
    position: absolute; font-family: "Raleway", sans-serif; font-weight: 700;
    color: var(--logo-ink); text-transform: uppercase; letter-spacing: 1px;
  }
  .brand--front { left: 470px; top: 300px; font-size: 22px; }
  .brand--back { left: 26px; top: 70px; font-size: 30px; }
  .front__band { position: absolute; left: 0; top: 0; width: 710px; height: 550px; }
  .contact {
    position: absolute; left: 302px; font-family: "Raleway", sans-serif;
    font-weight: 400; font-size: 19px; color: var(--paper); letter-spacing: 0.5px;
    text-transform: uppercase; display: flex; align-items: center; gap: 14px;
  }
  .contact--name { top: 412px; }
  .contact--mail { top: 454px; font-size: 17px; }
  .contact--phone { top: 497px; }

  /* back */
  .back__supplies {
    position: absolute; left: 346px; top: 19px; width: 182px; height: 155px;
    background: linear-gradient(135deg, #e05a8a 0%, #f3c840 40%, #6cc0e0 70%, #f5f1d6 100%);
    border-radius: 8px;
  }
  .back__stamp {
    position: absolute; left: 541px; top: 28px; width: 142px; height: 131px;
    border: 2px dotted var(--line);
  }
  .back__panel {
    position: absolute; left: 0; top: 174px; width: 344px; height: 376px;
    background: linear-gradient(135deg, var(--purple-dark) 0%, var(--purple) 55%, var(--purple-light) 100%);
  }
  .back__slogan {
    position: absolute; left: 0; top: 30px; width: 344px; text-align: center;
    font-family: "Cinzel", serif; font-size: 35px; line-height: 44px; color: var(--paper);
  }
  .back__cta {
    position: absolute; left: 0; top: 232px; width: 344px; text-align: center;
    font-family: "Raleway", sans-serif; font-weight: 700; color: var(--paper);
  }
  .back__cta-label { font-size: 17px; letter-spacing: 0.5px; }
  .back__cta-number { font-size: 27px; letter-spacing: 1px; margin-top: 2px; }
  .address-line {
    position: absolute; left: 386px; width: 294px; height: 0; border-top: 1.5px solid var(--line);
  }
</style>
</head>
<body>
<main class="sheet">
  <section class="card card--front">
    <div class="front__hero" role="img" aria-label="Hand rolling bright green paint over a white wall beneath a blurred rainbow of colour"></div>
    <h1 class="front__headline">BRING <span class="c1">C</span><span class="c2">O</span><span class="c3">L</span><span class="c4">O</span><span class="c5">R</span><br>TO YOUR HOME</h1>
    <p class="front__tagline">LICENSED AND INSURED</p>
    <div class="front__photo" role="img" aria-label="Smiling painter in white overalls holding a paint roller in a room under renovation"></div>
    <p class="brand brand--front">Marlow Painting</p>
    <svg class="front__band" viewBox="0 0 710 550" aria-hidden="true">
      <defs>
        <linearGradient id="bandFill" x1="0" y1="1" x2="1" y2="0">
          <stop offset="0" stop-color="#5a3a82"/>
          <stop offset="1" stop-color="#8a4c98"/>
        </linearGradient>
      </defs>
      <polygon points="262,385 710,385 710,550 203,550" fill="url(#bandFill)"/>
    </svg>
    <p class="contact contact--name">Ray Pettibone</p>
    <p class="contact contact--mail">
      <svg width="20" height="14" viewBox="0 0 20 14" aria-hidden="true"><rect x="0.5" y="0.5" width="19" height="13" fill="none" stroke="#fff" stroke-width="1.5"/><polyline points="1,1 10,8 19,1" fill="none" stroke="#fff" stroke-width="1.5"/></svg>
      pettiboneworks@brushmail.example
    </p>
    <p class="contact contact--phone">
      <svg width="20" height="18" viewBox="0 0 20 18" aria-hidden="true"><path d="M1 5 Q10 -1 19 5 L17 8 L14 6 L14 4 Q10 2 6 4 L6 6 L3 8 Z" fill="#fff"/><rect x="4" y="9" width="12" height="8" rx="1.5" fill="#fff"/><circle cx="10" cy="13" r="2" fill="#6a4288"/></svg>
      9145820731
    </p>
  </section>

  <section class="card card--back">
    <p class="brand brand--back">Marlow Painting</p>
    <div class="back__supplies" role="img" aria-label="Paint cans, brushes and an open colour swatch fan"></div>
    <div class="back__stamp" aria-hidden="true"></div>
    <div class="back__panel">
      <h2 class="back__slogan">OUR JOB’S<br>NOT COMPLETE<br>UNTIL YOU’RE<br>SATISFIED</h2>
      <div class="back__cta">
        <p class="back__cta-label">CALL NOW</p>
        <p class="back__cta-number">9145820731</p>
      </div>
    </div>
    <div class="address-line" style="top:278px"></div>
    <div class="address-line" style="top:321px"></div>
    <div class="address-line" style="top:365px"></div>
    <div class="address-line" style="top:408px"></div>
  </section>
</main>
</body>
</html>
```